Vorapo Business Card

Need a double sided business card. Would like the business card to have the logo on one side and the employees details and business contact details on the other.

Business

```html
<!DOCTYPE html>
<html lang="en">
<head>
<meta charset="utf-8">
<title>Vorapo Business Card</title>
<link href="https://fonts.googleapis.com/css2?family=Lato:wght@300;400;700&display=swap" rel="stylesheet">
<style>
  :root {
    --stage: #d9d9d9;
    --slate-top: #474c55;
    --slate-bottom: #30343b;
    --accent: #d9473d;
    --accent-dark: #b8352d;
    --ink: #3a3d42;
    --paper: #f4f4f4;
    --paper-shade: #dcdcdc;
    --white: #ffffff;
    --muted: #b9bdc4;
  }
  * { box-sizing: border-box; margin: 0; padding: 0; }
  html, body { width: 1200px; height: 900px; overflow: hidden; }
  body {
    background: var(--stage);
    font-family: "Lato", Arial, sans-serif;
    position: relative;
  }
  .card {
    position: absolute;
    top: 170px;
    width: 330px;
    height: 560px;
    background: radial-gradient(ellipse at 50% 35%, var(--slate-top) 0%, var(--slate-bottom) 80%);
    box-shadow: 0 10px 30px rgba(0,0,0,0.25);
    overflow: hidden;
  }
  .card--details { left: 230px; }
  .card--brand { left: 640px; }

  .mark {
    display: block;
    width: 26px;
    height: 26px;
    background: var(--accent);
  }

  /* Details side */
  .person {
    position: absolute;
    top: 96px;
    left: 0; right: 0;
    text-align: center;
  }
  .person .mark { margin: 0 auto 22px; }
  .person__name {
    color: var(--white);
    font-weight: 700;
    font-size: 25px;
    letter-spacing: 0.5px;
  }
  .person__role {
    color: var(--muted);
    font-weight: 400;
    font-size: 12px;
    letter-spacing: 1.5px;
    margin-top: 4px;
  }
  .contact-list {
    position: absolute;
    top: 300px;
    left: 0; right: 0;
    list-style: none;
  }
  .contact-list__item {
    display: flex;
    align-items: center;
    height: 42px;
    background: linear-gradient(to bottom, var(--white) 0%, var(--paper) 60%, var(--paper-shade) 100%);
    border-bottom: 1px solid #cfcfcf;
  }
  .contact-list__icon {
    width: 42px;
    height: 42px;
    background: var(--accent);
    border-bottom: 1px solid var(--accent-dark);
    display: flex;
    align-items: center;
    justify-content: center;
    flex-shrink: 0;
  }
  .contact-list__text {
    padding-left: 18px;
    color: var(--ink);
    font-size: 14px;
  }

  /* Brand side */
  .brand {
    position: absolute;
    top: 88px;
    left: 0; right: 0;
    display: flex;
    flex-direction: column;
    align-items: center;
  }
  .brand__lockup {
    display: flex;
    align-items: center;
    gap: 12px;
  }
  .brand__name {
    color: var(--white);
    font-weight: 700;
    font-size: 30px;
  }
  .brand__slogan {
    color: var(--muted);
    font-size: 10px;
    margin-top: 6px;
    letter-spacing: 0.5px;
  }
  .social {
    position: absolute;
    right: 26px;
    bottom: 40px;
    list-style: none;
  }
  .social__item {
    display: flex;
    align-items: center;
    width: 160px;
    height: 22px;
    border: 1px solid rgba(255,255,255,0.45);
    margin-top: 8px;
  }
  .social__icon {
    width: 22px;
    height: 22px;
    margin: -1px 0 -1px -1px;
    background: var(--accent);
  }
  .social__text {
    color: var(--muted);
    font-size: 9px;
    padding-left: 8px;
  }
</style>
</head>
<body>

<section class="card card--details" aria-label="Details side">
  <div class="person">
    <span class="mark"></span>
    <h1 class="person__name">INNITI VORAPO</h1>
    <p class="person__role">ART DIRECTOR</p>
  </div>
  <ul class="contact-list">
    <li class="contact-list__item">
      <span class="contact-list__icon">
        <svg width="20" height="20" viewBox="0 0 24 24" aria-hidden="true"><path fill="#fff" d="M6.6 10.8c1.4 2.8 3.8 5.1 6.6 6.6l2.2-2.2c.3-.3.7-.4 1-.2 1.1.4 2.3.6 3.6.6.6 0 1 .4 1 1V20c0 .6-.4 1-1 1C10.6 21 3 13.4 3 4c0-.6.4-1 1-1h3.5c.6 0 1 .4 1 1 0 1.3.2 2.5.6 3.6.1.3 0 .7-.2 1z"/></svg>
      </span>
      <span class="contact-list__text">+2 (5550) 1037264</span>
    </li>
    <li class="contact-list__item">
      <span class="contact-list__icon">
        <svg width="20" height="20" viewBox="0 0 24 24" aria-hidden="true"><rect x="7" y="2" width="10" height="20" rx="1.5" fill="none" stroke="#fff" stroke-width="2"/><rect x="10" y="18" width="4" height="1.5" fill="#fff"/></svg>
      </span>
      <span class="contact-list__text">+2 (5550) 1037264</span>
    </li>
    <li class="contact-list__item">
      <span class="contact-list__icon">
        <svg width="22" height="20" viewBox="0 0 24 24" aria-hidden="true"><rect x="2" y="5" width="20" height="14" fill="none" stroke="#fff" stroke-width="2"/><path d="M2 5l10 8 10-8" fill="none" stroke="#fff" stroke-width="2"/></svg>
      </span>
      <span class="contact-list__text">info@vorapo-mail.com</span>
    </li>
    <li class="contact-list__item">
      <span class="contact-list__icon">
        <svg width="20" height="20" viewBox="0 0 24 24" aria-hidden="true"><circle cx="12" cy="12" r="9" fill="none" stroke="#fff" stroke-width="2"/><path d="M3 12h18M12 3c3 3 3 15 0 18M12 3c-3 3-3 15 0 18" fill="none" stroke="#fff" stroke-width="1.6"/></svg>
      </span>
      <span class="contact-list__text">www.vorapo-studio.com</span>
    </li>
    <li class="contact-list__item">
      <span class="contact-list__icon">
        <svg width="20" height="20" viewBox="0 0 24 24" aria-hidden="true"><path fill="#fff" d="M12 2a7 7 0 0 0-7 7c0 5 7 13 7 13s7-8 7-13a7 7 0 0 0-7-7zm0 9.5a2.5 2.5 0 1 1 0-5 2.5 2.5 0 0 1 0 5z"/></svg>
      </span>
      <span class="contact-list__text">88 Linden Row, Harbor City</span>
    </li>
  </ul>
</section>

<section class="card card--brand" aria-label="Brand side">
  <div class="brand">
    <div class="brand__lockup">
      <span class="mark"></span>
      <h2 class="brand__name">Vorapo</h2>
    </div>
    <p class="brand__slogan">slogan right here</p>
  </div>
  <ul class="social">
    <li class="social__item"><span class="social__icon"></span><span class="social__text">@vorapo page link</span></li>
    <li class="social__item"><span class="social__icon"></span><span class="social__text">@vorapo feed link</span></li>
  </ul>
</section>

</body>
</html>
```